Infectious Diseases Research Laboratory Needs Business Card

We need a business card for an academic research laboratory based in Kansas City called MORVEK. The full lab name is Microbial Dose-Response/Exposure Bridging Studies Laboratory, but this does not need to be incorporated. We study novel ways to optimize the treatment of multidrug-resistant bacterial infections ("superbugs") throughout the entire biomedical research spectrum (from benchtop to bedside). The name MORVEK is not only an acronym for our lab name, but also represents our desire to make discoveries and explore the unknown (the stars, if you well). It also serves as an ode to the state of Kansas motto where we are based, ad astra per aspera ("to the stars, through difficulty").

Target Market(s)

Pharmaceutical companies, researchers

Industry/Entity Type

Pharmaceutical

Contact Information for Business Card

The business card should incorporate and complement our new logo (see uploaded files). Double-sided designs are preferred. Looking for something modern, but professional.

Font styles to use
Sans Serif

Requirements
Must have
• Double-sided. One side would ideally be a solid color incorporating logo and the other should also have the logo (smaller), but incorporate staff information.
• Color codes:
• Red: #F04C51
• Blue: #3477B5
• Gray: #808285

```html
<!DOCTYPE html>
<html lang="en">
<head>
<meta charset="utf-8">
<title>MORVEK Business Card</title>
<link href="https://fonts.googleapis.com/css2?family=Open+Sans:wght@400;600;700&display=swap" rel="stylesheet">
<style>
  :root {
    --red: #F04C51;
    --blue: #3477B5;
    --gray: #808285;
    --white: #ffffff;
    --backdrop: #ecebe9;
  }
  * { margin: 0; padding: 0; box-sizing: border-box; }
  html, body { width: 1200px; height: 900px; overflow: hidden; }
  body {
    position: relative;
    background: var(--backdrop);
    font-family: "Open Sans", Arial, sans-serif;
  }
  .card {
    position: absolute;
    overflow: hidden;
    box-shadow: 0 6px 18px rgba(0,0,0,0.15);
  }
  .card-front { left: 177px; top: 75px; width: 590px; height: 362px; background: var(--white); }
  .card-back  { left: 388px; top: 505px; width: 567px; height: 352px; background: var(--red); }
  .front-shapes { position: absolute; inset: 0; }
  .brand {
    position: absolute;
    left: 113px; top: 62px;
    display: flex; align-items: center; gap: 22px;
  }
  .brand-dot {
    width: 78px; height: 78px; border-radius: 50%;
    background: var(--blue);
  }
  .brand-name {
    font-weight: 600;
    font-size: 60px;
    letter-spacing: 4px;
    color: var(--red);
    line-height: 1;
  }
  .staff {
    position: absolute;
    right: 326px; top: 256px;
    text-align: right; color: var(--white);
  }
  .staff-name { font-weight: 700; font-size: 19px; line-height: 24px; }
  .staff-role { font-size: 15.5px; line-height: 22px; }
  .contacts {
    position: absolute;
    left: 285px; top: 245px;
    list-style: none; color: var(--white);
    font-size: 15.5px; line-height: 21.5px;
  }
  .contacts li { display: flex; align-items: center; gap: 11px; }
  .contacts svg { width: 13px; height: 13px; flex: none; }
  .address {
    position: absolute;
    left: 91px; top: 316px;
    color: var(--white); font-size: 15.5px;
  }
  .back-mark {
    position: absolute;
    left: 363px; top: 141px;
    width: 62px; height: 62px; border-radius: 50%;
    background: var(--white);
  }
</style>
</head>
<body>

<section class="card card-front" aria-label="Card front">
  <svg class="front-shapes" viewBox="0 0 590 362" aria-hidden="true">
    <polygon points="0,216 388,216 415,178 590,178 590,362 0,362" fill="var(--red)"/>
    <polygon points="0,188 402,188 384,212 0,212" fill="var(--blue)"/>
  </svg>

  <div class="brand">
    <span class="brand-dot" aria-hidden="true"></span>
    <span class="brand-name">MORVEK</span>
  </div>

  <div class="staff">
    <p class="staff-name">DANA WHITFIELD</p>
    <p class="staff-role">Managing Director</p>
  </div>

  <ul class="contacts">
    <li>
      <svg viewBox="0 0 16 16" aria-hidden="true"><path fill="#fff" d="M3.6 1l2.6 3-1.5 1.9c.9 2 2.4 3.5 4.4 4.4l1.9-1.5 3 2.6-1.6 2.6C7 14 2 9 1 3.2z"/></svg>
      044-555 018 274
    </li>
    <li>
      <svg viewBox="0 0 16 16" aria-hidden="true"><rect x="1" y="3" width="14" height="10" fill="#fff"/><path d="M1 3l7 6 7-6" fill="none" stroke="var(--red)" stroke-width="1.4"/></svg>
      info@morveklab.org
    </li>
    <li>
      <svg viewBox="0 0 16 16" aria-hidden="true"><circle cx="8" cy="8" r="6.5" fill="none" stroke="#fff" stroke-width="1.5"/><path d="M1.5 8h13M8 1.5c-3 3.5-3 9.5 0 13M8 1.5c3 3.5 3 9.5 0 13" fill="none" stroke="#fff" stroke-width="1.2"/></svg>
      www.morveklab.org
    </li>
  </ul>

  <p class="address">4410 Research Court, Kansas City, United States, 64108.</p>
</section>

<section class="card card-back" aria-label="Card back">
  <span class="back-mark" aria-hidden="true"></span>
</section>

</body>
</html>
```